Software Company Business Card

We are looking for a new design of our business card. The design will also be used in the rest of our branding and marketing materials as we want to keep it all uniform. We sell POS software to fine/luxury jewelers and also offer other business services as well to help the jeweler manage their business and need something more updated, technical and fresh, preferably more on the masculine side. We do not want any designs with gems in them but if possible would like to incorporate the circle and arrow in the logo into the design, but not a requirement if you can't make it work. I would like to see a variety of the mix. The colors need to remain our blue and orange and the logo can not change. The squiggly lines have been used as our corporate identity for over 20 years and its time to update. Our company name is TELK (Superior Counter Operations Platforms).

Target Market(s)

High End Jewelers

Industry/Entity Type

Software

Contact Information for Business Card

As seen in attached image

Requirements
Must have
• Our logo and the colors must remain the same. Blue is #d95d39 and Orange is #0f5682.
Nice to have
• The circle and arrow incorporated but not a requirement.
Should not have
• Anything jewelry or gem related.

```html
<!DOCTYPE html>
<html lang="en">
<head>
<meta charset="utf-8">
<title>TELK Business Card</title>
<link href="https://fonts.googleapis.com/css2?family=Montserrat:wght@600;800&family=Arimo:wght@400&display=swap" rel="stylesheet">
<style>
  :root {
    --brand-blue: #0f5682;
    --brand-blue-light: #1a7cbf;
    --brand-blue-dark: #0a3d5e;
    --brand-orange: #d95d39;
    --ink: #2a2a2a;
    --paper: #ffffff;
    --stage: #3a3a3a;
    --rule: #d4d4d4;
  }
  * { box-sizing: border-box; margin: 0; padding: 0; }
  html, body { width: 1200px; height: 1015px; overflow: hidden; }
  body {
    background: var(--stage);
    font-family: "Arimo", Arial, sans-serif;
    position: relative;
  }
  .card {
    position: absolute;
    left: 320px;
    width: 560px;
    height: 320px;
    box-shadow: 0 10px 30px rgba(0,0,0,0.45);
    overflow: hidden;
  }
  /* Back of card */
  .card-back { top: 150px; }
  .card-back .pattern-field {
    position: absolute; inset: 0;
    background: linear-gradient(200deg, var(--brand-blue-light) 0%, var(--brand-blue) 50%, var(--brand-blue-dark) 100%);
  }
  .card-back .wordmark {
    position: absolute; left: 205px; top: 130px;
    display: flex; align-items: center; gap: 16px;
  }
  .wordmark-name {
    font-family: "Montserrat", Arial, sans-serif;
    font-weight: 800;
    font-size: 62px;
    letter-spacing: -1px;
    line-height: 1;
  }
  .wordmark-dot {
    width: 46px; height: 46px; border-radius: 50%;
    background: var(--brand-orange);
  }
  .card-back .wordmark-name { color: var(--paper); }

  /* Front of card */
  .card-front { top: 545px; background: var(--paper); }
  .card-front .wordmark {
    position: absolute; left: 40px; top: 128px;
    display: flex; align-items: center; gap: 14px;
  }
  .card-front .wordmark-name { color: var(--brand-blue); font-size: 58px; }
  .card-front .wordmark-dot { width: 42px; height: 42px; }
  .divider {
    position: absolute; left: 262px; top: 30px;
    width: 1px; height: 260px;
    background: linear-gradient(var(--paper), var(--rule) 20%, var(--rule) 80%, var(--paper));
  }
  .contact { position: absolute; left: 290px; top: 56px; }
  .contact-name {
    font-family: "Montserrat", Arial, sans-serif;
    font-weight: 600; font-size: 22px;
    color: var(--brand-blue); line-height: 1.1;
  }
  .contact-title {
    font-size: 15px; color: var(--brand-orange);
    margin-bottom: 12px;
  }
  .contact-list { list-style: none; }
  .contact-list li {
    display: flex; align-items: center; gap: 8px;
    font-size: 13.5px; color: var(--ink);
    height: 22px;
  }
  .contact-list .accent { color: var(--brand-blue); }
  .icon {
    width: 16px; height: 16px; border-radius: 50%;
    background: var(--brand-orange);
    display: inline-flex; align-items: center; justify-content: center;
    flex: none;
  }
  .icon svg { width: 10px; height: 10px; }
  .address {
    margin-top: 10px; font-size: 13.5px; color: var(--ink); line-height: 1.35;
  }
</style>
</head>
<body>

<section class="card card-back">
  <div class="pattern-field" role="img" aria-label="Repeating field of embossed circle marks in tonal blues"></div>
  <div class="wordmark">
    <span class="wordmark-name">TELK</span>
    <span class="wordmark-dot"></span>
  </div>
</section>

<section class="card card-front">
  <div class="wordmark">
    <span class="wordmark-name">TELK</span>
    <span class="wordmark-dot"></span>
  </div>
  <div class="divider"></div>
  <div class="contact">
    <p class="contact-name">Dorian Westcott</p>
    <p class="contact-title">Director of Global Operations</p>
    <ul class="contact-list">
      <li><span class="icon"><svg viewBox="0 0 10 10"><path d="M2 1 L3.5 1 L4 3 L3 3.8 Q4 6 6.2 7 L7 6 L9 6.5 L9 8 Q9 9 8 9 Q1 8.5 1 2 Q1 1 2 1 Z" fill="#fff"/></svg></span>+ 800 555-0142</li>
      <li><span class="icon"><svg viewBox="0 0 10 10"><rect x="3" y="1" width="4" height="3" fill="#fff"/><rect x="1" y="4" width="8" height="4" rx="1" fill="#fff"/><rect x="3" y="6.5" width="4" height="2.5" fill="#fff" stroke="#d95d39" stroke-width="0.6"/></svg></span>+1 702 555-0187</li>
      <li><span class="icon"><svg viewBox="0 0 10 10"><rect x="1" y="2.5" width="8" height="5" fill="#fff"/><path d="M1 2.5 L5 5.5 L9 2.5" fill="none" stroke="#d95d39" stroke-width="0.8"/></svg></span>dorian@telkpos.com</li>
      <li><span class="icon"><svg viewBox="0 0 10 10"><circle cx="5" cy="5" r="3.8" fill="none" stroke="#fff" stroke-width="0.9"/><ellipse cx="5" cy="5" rx="1.6" ry="3.8" fill="none" stroke="#fff" stroke-width="0.8"/><line x1="1.2" y1="5" x2="8.8" y2="5" stroke="#fff" stroke-width="0.8"/></svg></span>www.<span class="accent">telkpos</span>.com</li>
    </ul>
    <p class="address">1840 Meridian Parkway Suite 210<br>Carson Ridge, NV 89500,USA</p>
  </div>
</section>

</body>
</html>
```